Fixing all glass products,fitting security doors,flyscreens,splashbacks,glazing

Looking for perhaps a liitle happy chap carrying a glass panel with crach throught it and maybe the pane of glass 'hurting' so it had 'pain'???
Open to suggestions

Industry/Entity Type

Security

Contact Information for Business Card

Brisk Corner Fitters
Darren Holloway
Specialising in security doors,flyscreens,splashbacks
0417362048
darrenholloway518@mailbrook.net

```html
<!DOCTYPE html>
<html lang="en">
<head>
<meta charset="utf-8">
<title>Brisk Corner Fitters – Business Card</title>
<link rel="stylesheet" href="https://fonts.googleapis.com/css2?family=Noto+Sans:wght@400&family=PT+Sans:wght@400;700&display=swap">
<style>
  :root {
    --backdrop: #4a4a4c;
    --card-white: #ffffff;
    --card-haze: #e6e7e9;
    --title-blue: #1a72b8;
    --band-deep: #2249a0;
    --band-mid: #1f86cf;
    --band-bright: #1aa6e2;
    --band-rim: #3a3b3f;
    --band-text: #ffffff;
    --art-light: #d9dbde;
    --art-dark: #6f6b68;
  }
  * { margin: 0; padding: 0; box-sizing: border-box; }
  html, body {
    width: 1200px;
    height: 999px;
    overflow: hidden;
    background: var(--backdrop);
  }
  .business-card {
    position: absolute;
    left: 68px;
    top: 192px;
    width: 1064px;
    height: 614px;
    overflow: hidden;
    background: linear-gradient(180deg, var(--card-haze) 0%, var(--card-white) 22%);
  }
  .card-band {
    position: absolute;
    left: 0;
    top: 0;
    width: 1064px;
    height: 614px;
  }
  .brand-block {
    position: absolute;
    left: 62px;
    top: 88px;
    font-family: "Noto Sans", sans-serif;
    color: var(--title-blue);
    font-size: 66px;
    line-height: 88px;
    font-weight: 400;
    letter-spacing: 0.5px;
  }
  .mascot-art {
    position: absolute;
    left: 735px;
    top: 46px;
    width: 278px;
    height: 344px;
    border-radius: 6px;
    background: linear-gradient(160deg, var(--art-light) 0%, #b9bcc0 55%, var(--art-dark) 100%);
  }
  .services {
    position: absolute;
    left: 42px;
    top: 460px;
    font-family: "PT Sans", sans-serif;
    color: var(--band-text);
    font-size: 27px;
    line-height: 37px;
  }
  .services-heading { font-weight: 700; }
  .contact-list {
    position: absolute;
    left: 542px;
    top: 474px;
    list-style: none;
    font-family: "PT Sans", sans-serif;
    color: var(--band-text);
    font-size: 27px;
    line-height: 46px;
    white-space: nowrap;
  }
  .contact-item {
    display: flex;
    align-items: center;
    gap: 16px;
  }
  .contact-icon { width: 26px; height: 26px; flex: none; }
</style>
</head>
<body>
  <section class="business-card">
    <svg class="card-band" viewBox="0 0 1064 614" aria-hidden="true">
      <defs>
        <radialGradient id="bandGlow" cx="50%" cy="62%" r="62%">
          <stop offset="0%" stop-color="var(--band-bright)"/>
          <stop offset="55%" stop-color="var(--band-mid)"/>
          <stop offset="100%" stop-color="var(--band-deep)"/>
        </radialGradient>
      </defs>
      <path d="M0 434 Q532 346 1064 434 L1064 614 L0 614 Z" fill="var(--band-rim)"/>
      <path d="M0 442 Q532 356 1064 442 L1064 614 L0 614 Z" fill="url(#bandGlow)"/>
    </svg>

    <h1 class="brand-block">
      <span class="brand-name">Brisk Corner Fitters</span><br>
      <span class="owner-name">Darren Holloway</span>
    </h1>

    <div class="mascot-art" role="img" aria-label="Cartoon glazier holding up a cracked glass pane in a metal frame"></div>

    <div class="services">
      <p class="services-heading">Specialising in</p>
      <p>security doors, flysvcreens</p>
      <p>splashbacks</p>
    </div>

    <ul class="contact-list">
      <li class="contact-item">
        <svg class="contact-icon" viewBox="0 0 24 24" aria-hidden="true">
          <path fill="#fff" d="M6.6 2.5c.6-.3 1.3-.1 1.6.5l1.6 3.2c.3.6.1 1.2-.4 1.6L8 8.9c.9 2.2 2.7 4.1 4.9 5l1.1-1.4c.4-.5 1.1-.6 1.6-.3l3.2 1.6c.6.3.8 1 .5 1.6l-1 2.1c-.4.8-1.3 1.3-2.2 1.1C9.9 17.4 5.4 12.6 4.4 6.5c-.1-.9.3-1.8 1.1-2.2z"/>
          <path fill="none" stroke="#fff" stroke-width="1.6" stroke-linecap="round" d="M14 3.5a7 7 0 0 1 6.5 6.5M14 7a3.5 3.5 0 0 1 3 3"/>
        </svg>
        <span>0417362048</span>
      </li>
      <li class="contact-item">
        <svg class="contact-icon" viewBox="0 0 24 24" aria-hidden="true">
          <path fill="#fff" d="M2 10 12 3l10 7v10a1 1 0 0 1-1 1H3a1 1 0 0 1-1-1z"/>
          <path fill="none" stroke="var(--band-mid)" stroke-width="1.6" d="M3 11l9 6 9-6"/>
        </svg>
        <span>darrenholloway518@mailbrook.net</span>
      </li>
    </ul>
  </section>
</body>
</html>
```